Marlo Vista Table & Chair Rentals

We need a business card for a table and chair rental company. We rent tables and chairs for weddings, funerals, business events and parties. We want something that looks clean and elegant while not being too busy. We would like colors in the green and blue hues and avoiding anything orange. We want to make sure the font is large enough to be seen easily.

Target Market(s)

Wedding & Event Rentals

Industry/Entity Type

Events

Contact Information for Business Card

Marlo Vista, sales@marlovistarentals.example, marlovistarentals.example, 360-555-0182

Requirements
Must have
• Easy to read font
Should not have
• Orange anywhere in the design

```html
<!DOCTYPE html>
<html lang="en">
<head>
<meta charset="utf-8">
<title>Marlo Vista Table &amp; Chair Rentals – Business Card</title>
<link href="https://fonts.googleapis.com/css2?family=Handlee&family=Dancing+Script:wght@500&family=Montserrat:wght@400;500&display=swap" rel="stylesheet">
<style>
  :root {
    --backdrop: #3a3a3c;
    --ink: #1d1a16;
    --brown: #3b3424;
    --green: #6e9a1f;
    --green-light: #8cb83a;
    --white: #ffffff;
    --photo-light: #f3f4f2;
    --photo-mid: #dfe3dc;
    --photo-green: #5f7a35;
    --photo-dark: #3c3a2c;
  }
  * { box-sizing: border-box; margin: 0; padding: 0; }
  html, body { width: 1200px; height: 852px; overflow: hidden; }
  body {
    background: var(--backdrop);
    display: flex;
    flex-direction: column;
    align-items: center;
    justify-content: center;
    gap: 40px;
    font-family: "Montserrat", sans-serif;
  }
  .card {
    position: relative;
    width: 525px;
    height: 300px;
    border-radius: 22px;
    overflow: hidden;
  }

  /* Front */
  .card-front .photo-area {
    position: absolute; inset: 0;
    background:
      radial-gradient(circle at 72% 45%, #f4f6f0 0 14%, #c9d3c4 22%, transparent 34%),
      radial-gradient(circle at 20% 58%, #e6e9e2 0 10%, transparent 20%),
      linear-gradient(160deg, var(--photo-light) 0%, var(--photo-mid) 40%, var(--photo-green) 78%, var(--photo-dark) 100%);
  }
  .card-front .brand {
    position: absolute;
    left: 0; right: 0; top: 92px;
    text-align: center;
    transform: translateX(-20px);
  }
  .card-front .brand-name {
    font-family: "Handlee", cursive;
    font-size: 64px;
    color: var(--ink);
    line-height: 1;
  }
  .card-front .brand-tagline {
    font-family: "Montserrat", sans-serif;
    font-size: 22px;
    color: var(--ink);
    margin-top: 8px;
    letter-spacing: 0.5px;
  }

  /* Back */
  .card-back .photo-area {
    position: absolute; inset: 0;
    background:
      radial-gradient(circle at 58% 38%, #ffffff 0 10%, #e9ece6 22%, transparent 36%),
      linear-gradient(100deg, #fbfbfa 0%, var(--photo-light) 45%, var(--photo-mid) 100%);
  }
  .card-back .shapes { position: absolute; inset: 0; }
  .card-back .brand-name {
    position: absolute;
    left: 36px; top: 64px;
    font-family: "Handlee", cursive;
    font-size: 56px;
    color: var(--ink);
    line-height: 1;
  }
  .contact-list {
    position: absolute;
    left: 36px; top: 166px;
    list-style: none;
  }
  .contact-list li {
    display: flex;
    align-items: center;
    gap: 12px;
    font-size: 14px;
    color: var(--ink);
    height: 27px;
  }
  .contact-list svg { width: 15px; height: 15px; fill: var(--ink); flex: none; }
  .card-back .side-tagline {
    position: absolute;
    right: 22px; top: 132px;
    font-family: "Dancing Script", cursive;
    font-size: 23px;
    color: var(--white);
    text-align: center;
    line-height: 1.4;
  }
</style>
</head>
<body>

<section class="card card-front">
  <div class="photo-area" role="img" aria-label="Photo of white hydrangea flower balls hanging from white event chairs along an aisle"></div>
  <div class="brand">
    <div class="brand-name">Marlo Vista</div>
    <div class="brand-tagline">Table and Chair Rentals</div>
  </div>
</section>

<section class="card card-back">
  <div class="photo-area" role="img" aria-label="Faded photo of white flowers and event chairs"></div>
  <svg class="shapes" viewBox="0 0 525 300" preserveAspectRatio="none" aria-hidden="true">
    <path d="M525 15 C450 20 415 80 385 135 C355 195 290 262 150 292 L140 300 L525 300 Z" fill="var(--brown)"/>
    <path d="M520 10 C440 15 402 75 372 132 C342 190 270 255 110 284 C262 250 330 192 360 136 C392 78 438 24 520 10 Z" fill="var(--green)"/>
    <path d="M500 26 C430 40 392 100 360 152 C325 210 250 262 70 294 C240 258 312 212 348 158 C382 104 428 48 500 26 Z" fill="var(--green-light)"/>
    <path d="M0 284 C90 274 170 272 250 262 C180 282 100 292 0 300 Z" fill="var(--green)"/>
  </svg>
  <div class="brand-name">Marlo Vista</div>
  <ul class="contact-list">
    <li>
      <svg viewBox="0 0 16 16"><path d="M3 2h3l1.5 3.5-2 1.3a9 9 0 0 0 3.7 3.7l1.3-2L14 10v3a1.5 1.5 0 0 1-1.5 1.5C7 14.5 1.5 9 1.5 3.5A1.5 1.5 0 0 1 3 2z"/></svg>
      360-555-0182
    </li>
    <li>
      <svg viewBox="0 0 16 16"><path d="M1 3h14v10H1z M2 4.2v.3l6 4.2 6-4.2v-.3z" fill-rule="evenodd"/></svg>
      sales@marlovistarentals.example
    </li>
    <li>
      <svg viewBox="0 0 16 16"><path d="M8 1a7 7 0 1 0 0 14A7 7 0 0 0 8 1zm0 1.5c.9 0 1.9 1.9 2.1 4.7H5.9C6.1 4.4 7.1 2.5 8 2.5zM2.6 7.2a5.5 5.5 0 0 1 2.7-4.1 10 10 0 0 0-.9 4.1zm0 1.6h1.8c.1 1.5.4 2.9.9 4.1a5.5 5.5 0 0 1-2.7-4.1zM8 13.5c-.9 0-1.9-1.9-2.1-4.7h4.2c-.2 2.8-1.2 4.7-2.1 4.7zm2.7-.6c.5-1.2.8-2.6.9-4.1h1.8a5.5 5.5 0 0 1-2.7 4.1zm.9-5.7c-.1-1.5-.4-2.9-.9-4.1a5.5 5.5 0 0 1 2.7 4.1z"/></svg>
      www.marlovistarentals.example
    </li>
  </ul>
  <div class="side-tagline">Table &amp;<br>Chair Rentals</div>
</section>

</body>
</html>
```